Infographic for a Christian church discipleship pathway

We need to take a fairly complex program that helps people in a Baptist church follow Jesus, and turn it into a simple graphic. This graphic does not have to explain the whole program, web pages and print materials will do that. But, it should be something that people see and understand what it is quickly. The attached graphic is only to give the key words and general direction of the program. It should not serve as a design guide. In other words, we want to see some other ideas how this information can be imparted graphically with concision and creativity. It's important to note, the categories at the top (pray daily, read daily, gather weekly) are first steps, starting points....one shouldn't move forward until they've incorporated these things into their life. However, the categories that follow (study, connect, serve, etc) are not necessarily steps to take in sequential order.

The diagrams we've provided are not what we expect. They are only to explain the program. Here is a verbal description: The motto of our church is "A Ready Church" (ready to serve, ready to love, ready for when Jesus returns). There are four words that describe a ready church member: FOCUSED on the return of Christ, FAITHFUL in a daily relationship with Jesus, PREPARED for any opportunity to be a supernatural vessel of God's worK, LOOKING to invite others into God's family. The first two are God's Work in Me (Focused and faithful); the second two are God's Work Through me (Prepared, looking). Please use those two things as you wish (Focused faithful prepared looking; and God's word in and through me). If they are clarifying, please use. If not, you don't have to use.

Additionally, the strategies we employ to be "a ready church" are 1. Prayer 2. God's Word, and 3. Biblical Community. (So, in other words, these three things help us be a people who is focused, faithful, prepared, and looking....which is a ready church.

To provide some information how we will build this out: this graphic will be used in print and digital content. The digital content will allow people to click on each category to access training and resources associated with that discipline. (Fasting, reflecting, etc).

www.qvd.church

Target Market(s)

35-50

Industry/Entity Type

Religious

Other font styles liked:
• Lato and/or Cambria

Requirements
Must have
• Fonts: lato, cambria. Colors#: 373E41, ebebe8, #a69677. Accent Colors: 80401D, #4e5730, #a5bac8
Nice to have
• A designer who has an understanding of what it means to incorporate the spiritual disciplines of the Christian faith into their life.

```html
<!DOCTYPE html>
<html lang="en">
<head>
<meta charset="utf-8">
<title>A Ready Church – Rhythms &amp; Practices</title>
<link rel="stylesheet" href="https://fonts.googleapis.com/css2?family=Poppins:wght@400;500;600;700&display=swap">
<style>
  :root {
    --ink: #373e41;
    --ink-deep: #2b3033;
    --slate: #6d787d;
    --tan: #a69677;
    --tan-deep: #7a6c55;
    --paper: #ffffff;
    --cell-light: #e3e3e2;
    --cell-mid: #d1d1d0;
    --text: #1c1c1c;
    --stage: #d8d8d8;
  }
  * { margin: 0; padding: 0; box-sizing: border-box; }
  html, body { width: 800px; height: 1200px; overflow: hidden; }
  body { background: var(--stage); font-family: "Poppins", sans-serif; position: relative; }

  .poster {
    position: absolute; left: 20px; top: 315px; width: 760px; height: 570px;
    background: var(--paper); box-shadow: 0 2px 8px rgba(0,0,0,.12); overflow: hidden;
  }

  .brand { position: absolute; left: 34px; top: 36px; display: flex; align-items: center; gap: 8px; }
  .brand-mark { width: 34px; height: 34px; background: var(--ink); flex: none; }
  .brand-name {
    font-weight: 700; font-size: 15px; line-height: 16px; color: var(--ink); text-transform: uppercase;
  }

  .title-cross { position: absolute; left: 212px; top: 24px; width: 50px; height: 80px; }
  .title-bar {
    position: absolute; left: 240px; top: 24px; width: 520px; height: 79px;
    background: var(--ink); color: #fff; padding: 7px 0 0 34px;
  }
  .title-main { font-weight: 700; font-size: 45px; line-height: 46px; letter-spacing: .5px; white-space: nowrap; }
  .title-sub { font-weight: 400; font-size: 18.5px; line-height: 20px; letter-spacing: .4px; white-space: nowrap; }

  .pathway-side { position: absolute; left: 38px; top: 119px; width: 100px; height: 410px; }
  .side-bg { position: absolute; inset: 0; width: 100%; height: 100%; }
  .side-label {
    position: absolute; writing-mode: vertical-rl; transform: rotate(180deg);
    color: #fff; text-align: center; white-space: nowrap;
  }
  .side-label strong { display: block; font-weight: 700; font-size: 15.5px; line-height: 20px; letter-spacing: .2px; }
  .side-label span { display: block; font-size: 8.5px; line-height: 12px; }
  .label-in { left: 22px; top: 14px; height: 172px; }
  .label-through { left: 22px; top: 218px; height: 184px; }
  .start-here {
    position: absolute; left: 74px; top: 44px; writing-mode: vertical-rl; transform: rotate(180deg);
    color: #e4e8ea; font-size: 12px; letter-spacing: 5px; white-space: nowrap;
  }

  .grid {
    position: absolute; left: 138px; top: 119px; width: 527px; height: 410px;
    display: grid; grid-template-columns: 175px 174px 178px;
    grid-template-rows: 68px 29px 82px 79px 76px 76px;
  }
  .head {
    color: #fff; text-align: center; display: flex; flex-direction: column; justify-content: center; padding: 0 14px;
  }
  .head h2 { font-weight: 600; font-size: 17px; line-height: 17px; text-transform: uppercase; }
  .head p { font-size: 7.5px; line-height: 9.5px; font-weight: 500; margin-top: 3px; }
  .tone-tan { background: var(--tan); }
  .tone-deep { background: var(--tan-deep); }
  .step {
    color: #fff; font-size: 9.5px; font-weight: 500; text-transform: uppercase;
    display: flex; align-items: center; justify-content: center; position: relative; z-index: 2;
  }
  .practice {
    display: flex; align-items: center; justify-content: center; position: relative;
    font-weight: 600; font-size: 14.5px; text-transform: uppercase; color: var(--text);
    border-right: 1px solid rgba(0,0,0,.06);
  }
  .practice::before {
    content: ""; position: absolute; top: 0; left: 50%; transform: translateX(-50%);
    border-left: 9px solid transparent; border-right: 9px solid transparent; border-top: 9px solid var(--notch);
  }
  .row-light { background: var(--cell-light); --notch: var(--cell-mid); }
  .row-mid { background: var(--cell-mid); --notch: var(--cell-light); }
  .after-tan { --notch: var(--tan); }
  .after-deep { --notch: var(--tan-deep); }

  .steeple-art {
    position: absolute; left: 672px; top: 112px; width: 88px; height: 417px;
    background: linear-gradient(180deg, rgba(166,150,119,.35) 0%, rgba(166,150,119,.75) 45%, var(--tan) 100%);
    border-radius: 44px 44px 0 0;
  }
</style>
</head>
<body>
  <main class="poster">
    <header>
      <div class="brand">
        <span class="brand-mark"></span>
        <div class="brand-name">Cedar Point<br>Chapel</div>
      </div>
      <svg class="title-cross" viewBox="0 0 50 80" role="img" aria-label="Wooden cross illustration">
        <rect x="0" y="0" width="50" height="80" fill="#a69677"/>
      </svg>
      <div class="title-bar">
        <h1 class="title-main">A READY CHURCH</h1>
        <p class="title-sub">RHYTHMS &amp; PRACTICES FOR A READY LIFE</p>
      </div>
    </header>

    <aside class="pathway-side">
      <svg class="side-bg" viewBox="0 0 100 410" preserveAspectRatio="none">
        <path d="M12 0 H100 V410 H0 V12 Q0 0 12 0Z" fill="#2b3033"/>
        <path d="M12 0 H100 V225 L0 150 V12 Q0 0 12 0Z" fill="#373e41"/>
        <path d="M69 0 H100 V225 L69 202Z" fill="#6d787d"/>
      </svg>
      <div class="side-label label-in"><strong>FOCUSED, FAITHFUL</strong><span>God's Work In Me</span></div>
      <div class="side-label label-through"><strong>PREPARED. LOOKING</strong><span>God's Work Through Me</span></div>
      <div class="start-here">START HERE</div>
    </aside>

    <section class="grid">
      <div class="head tone-tan"><h2>Prayer</h2><p>Become a person devoted to prayer each day of your life.</p></div>
      <div class="head tone-deep"><h2>God's Word</h2><p>Build a daily habit of beholding God in His Word.</p></div>
      <div class="head tone-tan"><h2>Biblical<br>Community</h2><p>Engage deeply in Christian community.</p></div>

      <div class="step tone-deep">Pray Daily</div>
      <div class="step tone-tan">Read Daily</div>
      <div class="step tone-deep">Gather Weekly</div>

      <div class="practice row-light after-deep">Rest</div>
      <div class="practice row-light after-tan">Study</div>
      <div class="practice row-light after-deep">Connect</div>

      <div class="practice row-mid">Reflect</div>
      <div class="practice row-mid">Memorize</div>
      <div class="practice row-mid">Learn</div>

      <div class="practice row-light">Fast</div>
      <div class="practice row-light">Teach</div>
      <div class="practice row-light">Give</div>

      <div class="practice row-mid">Intercede</div>
      <div class="practice row-mid">Proclaim</div>
      <div class="practice row-mid">Serve</div>
    </section>

    <div class="steeple-art" role="img" aria-label="Illustration of a church steeple with cross and bell tower"></div>
  </main>
</body>
</html>
```